Brisbane IT support business needs our first business card

Hello we are a Brisbane based Information Technology company providing support and services to small and medium sized businesses. We provide a range of services and solutions.

The business name is Wattleridge Computer Services Group, or WCSG for short.

I am looking for a business card that looks professional (don't we all want that), but most importantly, it most utilize the colours in the logo attached.

Other business owners seeking our IT services, and also home users.

Business

• Please only use the blue/orange colours in logo attached

```html
<!DOCTYPE html>
<html lang="en">
<head>
<meta charset="utf-8">
<title>WCSG Business Card</title>
<link href="https://fonts.googleapis.com/css2?family=Montserrat:wght@400;500;700;800&display=swap" rel="stylesheet">
<style>
  :root {
    --navy: #0f4777;
    --orange: #f26a14;
    --paper: #fbfbfb;
    --ink: #545c64;
    --stage: #e6eaea;
  }
  * { margin: 0; padding: 0; box-sizing: border-box; }
  html, body { width: 1200px; height: 1000px; overflow: hidden; }
  body {
    background: var(--stage);
    font-family: "Montserrat", Arial, sans-serif;
    position: relative;
  }
  .card {
    position: absolute;
    width: 540px;
    height: 310px;
    background: var(--paper);
    overflow: hidden;
    box-shadow: 0 6px 18px rgba(0,0,0,0.12);
  }
  .card--front { left: 40px; top: 230px; }
  .card--back { left: 620px; top: 460px; }

  /* Front */
  .front__band {
    position: absolute; left: 0; right: 0; top: 62px; height: 38px;
    background: var(--orange);
  }
  .front__brand {
    position: absolute; left: 26px; top: 14px;
    font-size: 56px; font-weight: 800; line-height: 1;
    color: var(--orange); letter-spacing: 1px;
    text-shadow: none;
  }
  .front__brand-backing {
    position: absolute; left: 18px; top: 58px; width: 190px; height: 14px;
    background: var(--paper);
  }
  .front__name {
    position: absolute; right: 28px; top: 71px;
    color: #fff; font-weight: 700; font-size: 17px;
  }
  .front__role {
    position: absolute; right: 28px; top: 104px;
    color: var(--ink); font-size: 12px; font-weight: 500;
  }
  .front__contact {
    position: absolute; right: 28px; top: 128px;
    list-style: none; text-align: right;
    color: var(--ink); font-size: 13.5px; line-height: 21px;
  }
  .front__contact .address { margin-bottom: 4px; }
  .front__mark {
    position: absolute; left: 150px; top: 150px;
  }
  .front__footer {
    position: absolute; left: 0; right: 0; bottom: 0; height: 66px;
    background: var(--navy);
    display: flex; align-items: center; justify-content: flex-end;
    padding-right: 36px;
  }
  .web {
    color: #fff; font-weight: 700; font-size: 19px; letter-spacing: 0.5px;
  }

  /* Back */
  .back__lockup {
    position: absolute; left: 60px; top: 70px;
    display: flex; align-items: center;
  }
  .back__divider {
    width: 2px; height: 82px; background: var(--orange);
    margin: 0 16px 0 24px;
  }
  .back__name {
    color: var(--orange); font-weight: 700;
  }
  .back__name .short { display: block; font-size: 58px; line-height: 0.9; letter-spacing: 1px; }
  .back__name .long { display: block; font-size: 10.5px; line-height: 12px; margin-top: 6px; text-transform: uppercase; width: 180px; }
  .back__sweep { position: absolute; left: 0; bottom: 0; }
  .back__web {
    position: absolute; right: 96px; bottom: 34px;
    transform: rotate(-10deg);
  }
</style>
</head>
<body>

<section class="card card--front" aria-label="Business card front">
  <div class="front__band"></div>
  <div class="front__brand">WCSG</div>
  <div class="front__name">Daniel Harrow</div>
  <div class="front__role">manager</div>
  <ul class="front__contact">
    <li class="address">48 Creek Lane, Milton QLD 4064</li>
    <li>t: 3105 2281</li>
    <li>m: 3105 2281</li>
    <li>e: hello@wcsg-it.com</li>
  </ul>
  <svg class="front__mark" width="124" height="100" viewBox="0 0 124 100" aria-hidden="true">
    <circle cx="62" cy="62" r="60" fill="var(--navy)"/>
  </svg>
  <div class="front__footer"><span class="web">www.wcsg-it.com</span></div>
</section>

<section class="card card--back" aria-label="Business card back">
  <div class="back__lockup">
    <svg width="124" height="124" viewBox="0 0 124 124" aria-hidden="true">
      <circle cx="62" cy="62" r="60" fill="var(--navy)"/>
    </svg>
    <div class="back__divider"></div>
    <div class="back__name">
      <span class="short">WCSG</span>
      <span class="long">Wattleridge Computer Services Group</span>
    </div>
  </div>
  <svg class="back__sweep" width="540" height="150" viewBox="0 0 540 150" aria-hidden="true">
    <path d="M0 118 Q270 96 540 0" fill="none" stroke="var(--orange)" stroke-width="2"/>
    <path d="M0 126 Q270 104 540 12 L540 150 L0 150 Z" fill="var(--navy)"/>
  </svg>
  <span class="web back__web">www.wcsg-it.com</span>
</section>

</body>
</html>
```